Dietitian needs awesome business card

I need a contemporary design that's eye catching but professional.
My card is to given to doctors, specialists and patients alike.
I manage patients with chronic diseases
I have uploaded my logo and current business card, I would also like the other Certified Clinical Nutrition Adviser logo incorporated into the design

Target Market(s)

Doctors, specialists and patients

Industry/Entity Type

Healthcare

Contact Information for Business Card

www.brindlewaynutrition.com.au
Ph: 0427 514 903
Fax: 6482 7150
email: marcus.t.wellbeing@corvalmail.com
Space on the back of the card with: Appointment date, Appointment time and appointment location

Font styles to use
Serif

Colors
fbee3e
876aae
ffc214

Requirements
Must have
• My Logo
• Certified Clinical Nutrition Adviser Logo
• My 4 locations - Harrowfield Medical Centre, North Pellin Health, Kestwick Medical, Fernbrook Doctors Surgery
Nice to have
• I like the colours in my current business card

```html
<!DOCTYPE html>
<html lang="en">
<head>
<meta charset="utf-8">
<title>Brindleway Nutrition &amp; Dietetics – Business Card</title>
<link rel="stylesheet" href="https://fonts.googleapis.com/css2?family=Philosopher:wght@400;700&family=Open+Sans:ital,wght@0,400;0,600;1,400&display=swap">
<style>
  :root {
    --backdrop: #e6e6e6;
    --card: #ffffff;
    --navy: #1f2f86;
    --label-blue: #2b4aa0;
    --green: #8cc63f;
    --ink: #4a4a4a;
    --rule: #9a9a9a;
    --badge: #f47b20;
    --check: #3d5aa8;
  }
  * { box-sizing: border-box; margin: 0; padding: 0; }
  html, body {
    width: 1105px; height: 1200px; overflow: hidden;
    background: var(--backdrop);
  }
  .canvas { position: relative; width: 1105px; height: 1200px; }
  .card {
    position: absolute; left: 180px; width: 746px; height: 427px;
    background: var(--card);
  }
  .card--front { top: 119px; }
  .card--back { top: 637px; }

  /* front */
  .brand {
    position: absolute; left: 160px; top: 86px;
    display: flex; align-items: center; gap: 26px;
  }
  .brand__mark {
    width: 104px; height: 104px; border-radius: 50%;
    background: var(--navy); flex: none;
  }
  .brand__name {
    font-family: "Philosopher", sans-serif; font-weight: 400;
    font-size: 44px; line-height: 1.05; color: var(--navy);
  }
  .front-rule {
    position: absolute; left: 43px; right: 43px; top: 283px;
    border-top: 2px solid var(--navy);
  }
  .person { position: absolute; left: 43px; top: 296px; }
  .person__name {
    font-family: "Philosopher", sans-serif; font-size: 27px; color: var(--navy);
    line-height: 34px;
  }
  .person__role {
    font-family: "Philosopher", sans-serif; font-size: 21px; color: var(--green);
    line-height: 30px; padding-left: 2px;
  }
  .person__email {
    font-family: "Open Sans", sans-serif; font-style: italic; font-size: 17px;
    color: var(--ink); line-height: 30px; padding-left: 2px;
  }
  .contact {
    position: absolute; right: 43px; top: 300px; text-align: right;
    font-family: "Open Sans", sans-serif; font-size: 18px; color: var(--ink);
    line-height: 30px;
  }
  .contact__label { font-weight: 600; }

  /* back */
  .note-line {
    position: absolute; left: 50px; right: 53px;
    border-top: 1.5px solid var(--rule);
  }
  .appointment {
    position: absolute; left: 50px; right: 53px; top: 212px;
    display: flex; align-items: baseline;
    font-family: "Open Sans", sans-serif; color: var(--label-blue);
  }
  .appointment__label { font-size: 21px; white-space: nowrap; }
  .appointment__fill {
    border-bottom: 2px dotted var(--label-blue); margin: 0 8px 0 10px;
    height: 1px; align-self: flex-end; margin-bottom: 7px;
  }
  .appointment__fill--date { width: 285px; margin-right: 20px; }
  .appointment__fill--time { flex: 1; }
  .appointment__suffix { font-size: 15px; }
  .back-mark {
    position: absolute; left: 47px; top: 287px;
    width: 82px; height: 82px; border-radius: 50%; background: var(--navy);
  }
  .credential-badge {
    position: absolute; left: 164px; top: 290px; width: 179px; height: 83px;
    background: var(--badge); border-radius: 3px;
  }
  .locations {
    position: absolute; left: 397px; top: 276px; list-style: none;
    font-family: "Open Sans", sans-serif; font-size: 19.5px; color: var(--ink);
  }
  .locations li { display: flex; align-items: center; height: 27px; }
  .locations li::before {
    content: ""; width: 15px; height: 15px; border: 1.5px solid var(--check);
    margin-right: 16px; flex: none;
  }
</style>
</head>
<body>
<main class="canvas">
  <section class="card card--front" aria-label="Business card front">
    <div class="brand">
      <span class="brand__mark" aria-hidden="true"></span>
      <div class="brand__name">Brindleway<br>Nutrition &amp; Dietetics</div>
    </div>
    <div class="front-rule"></div>
    <div class="person">
      <p class="person__name">Marcus Tolland</p>
      <p class="person__role">Nutritionist &amp; Chef</p>
      <p class="person__email">marcus.t.wellbeing@corvalmail.com</p>
    </div>
    <div class="contact">
      <p><span class="contact__label">Phone:</span> 0427 514 903</p>
      <p><span class="contact__label">Fax:</span> 6482 7150</p>
      <p>www.brindlewaynutrition.com.au</p>
    </div>
  </section>

  <section class="card card--back" aria-label="Business card back">
    <div class="note-line" style="top:54px"></div>
    <div class="note-line" style="top:94px"></div>
    <div class="note-line" style="top:135px"></div>
    <div class="note-line" style="top:178px"></div>
    <div class="appointment">
      <span class="appointment__label">Date :</span>
      <span class="appointment__fill appointment__fill--date"></span>
      <span class="appointment__label">Time :</span>
      <span class="appointment__fill appointment__fill--time"></span>
      <span class="appointment__suffix">AM/PM</span>
    </div>
    <span class="back-mark" aria-hidden="true"></span>
    <span class="credential-badge" role="img" aria-label="Certified Clinical Nutrition Adviser badge"></span>
    <ul class="locations">
      <li>Harrowfield Medical Centre</li>
      <li>North Pellin Health</li>
      <li>Kestwick Medical</li>
      <li>Fernbrook Doctors Surgery</li>
    </ul>
  </section>
</main>
</body>
</html>
```